Etiketten-Design für Eierschachtel
Zielgruppe
Wir haben einen Hofladen, indem wir unsere hofeigenen Produkte direkt an den Verbraucher verkaufen.
Aufgabenstellung
Wir suchen ein Etikett für unsere Eierschachtel, die wir für den Verkauf unserer Eier im eigenen Hofladen benötigen.
Das Etikett soll hell und freundlich, aber keinesfalls überladen oder zu verspielt sein. Es soll die Natürlichkeit und Regionalität widerspiegeln. Wir halten unsere Hühner in mobiler Freilandhaltung mit ausreichend Auslauf auf unseren Wiesen.
Das beigefügte Logo (einmal farbig, einmal schwarz/weiß - je nach Vorschlag was besser passt) soll integriert werden.
Das Etikett soll folgende Punkte enthalten:
Rückseite:
- 'Verbraucherhinweis: Nach dem Kauf bei Kühlschranktemperatur aufbewahren. Nach Ablauf des
Mindesthaltbarkeitsdatums durcherhitzen.'
- Familie Haslbeck
Lindenweg 7
84273 Auwiesen
Vorderseite (zum Öffnen der Eierschachtel) bzw. Deckel oben:
- '10 frische Eier aus mobiler Freilandhaltung' (gerne auch eigene Vorschläge von Ihnen)
- passender Slogan, der auf Regionalität bzw. Einkaufen direkt beim Erzeuger basiert
Format: ca. 21,4cm breit und ca. 14,2cm lang

```html
<!DOCTYPE html>
<html lang="de">
<head>
<meta charset="utf-8">
<title>Eierschachtel-Etikett – Haslbeck Hof</title>
<link rel="stylesheet" href="https://fonts.googleapis.com/css2?family=Abril+Fatface&family=Nunito+Sans:wght@600;700;800&display=swap">
<style>
  :root {
    --meadow-light: #dde7d9;
    --meadow-soft: #e6ede3;
    --farm-green: #3a7d3e;
    --wheat-brown: #a07c50;
    --ink: #1d1d1b;
    --paper: #ffffff;
    --cut-line: #1a1a1a;
  }
  * { margin: 0; padding: 0; box-sizing: border-box; }
  html, body {
    width: 1200px; height: 821px; overflow: hidden;
    background: var(--paper);
  }
  .label {
    position: relative; width: 1200px; height: 821px;
    font-family: "Nunito Sans", Arial, sans-serif; color: var(--ink);
  }
  .dieline { position: absolute; inset: 0; }
  .line {
    position: absolute; text-align: center; white-space: nowrap;
  }
  .back-side { transform: rotate(180deg); left: 0; width: 1150px; }
  .back-address { top: 176px; font-size: 24px; font-weight: 700; letter-spacing: .3px; }
  .back-address .dot { margin: 0 16px; }
  .back-title { top: 117px; font-size: 17px; font-weight: 800; }
  .back-note-1 { top: 90px; font-size: 15.5px; font-weight: 600; }
  .back-note-2 { top: 61px; font-size: 15.5px; font-weight: 600; }
  .farm-name {
    left: 0; width: 1170px; top: 381px;
    font-size: 19px; font-weight: 700; letter-spacing: 1px;
    color: var(--farm-green);
  }
  .product-count {
    left: 0; width: 1150px; top: 430px;
    font-family: "Abril Fatface", Georgia, serif; font-size: 60px; line-height: 1;
  }
  .product-claim {
    left: 0; width: 1150px; top: 506px;
    font-size: 28px; font-weight: 700;
  }
  .slogan {
    left: 0; width: 1150px; top: 658px;
    font-size: 31px; font-weight: 700; color: var(--wheat-brown);
  }
</style>
</head>
<body>
<div class="label">
  <svg class="dieline" width="1200" height="821" viewBox="0 0 1200 821">
    <defs>
      <clipPath id="box-shape">
        <path id="outline-path" d="M91,62 Q91,44 109,44 L1082,44 Q1100,44 1100,62 L1100,190 L1149,249 L1149,490 L1100,541 L1100,578 C1100,610 1060,626 1000,628 L895,629 Q878,629 878,646 L878,716 Q878,732 862,732 L287,732 Q271,732 271,716 L271,646 Q271,629 254,629 L200,628 C140,626 91,610 91,578 L91,541 L44,490 L44,249 L91,190 Z"/>
      </clipPath>
      <linearGradient id="meadow-fade" x1="0" y1="0" x2="0" y2="1">
        <stop offset="0" stop-color="#ffffff"/>
        <stop offset="1" stop-color="#e1e9dd"/>
      </linearGradient>
    </defs>
    <g clip-path="url(#box-shape)">
      <rect class="back-panel" x="0" y="0" width="1200" height="249" fill="var(--meadow-light)"/>
      <rect class="green-band" x="0" y="249" width="1200" height="44" fill="var(--farm-green)"/>
      <rect class="front-panel" x="0" y="293" width="1200" height="440" fill="var(--paper)"/>
      <rect class="meadow-grass" role="img" aria-label="Zarte Wiesengräser als heller Hintergrund" x="0" y="380" width="1200" height="360" fill="url(#meadow-fade)"/>
      <line x1="0" y1="318" x2="1200" y2="318" stroke="var(--wheat-brown)" stroke-width="3"/>
    </g>
    <line class="back-divider" x1="340" y1="151" x2="808" y2="151" stroke="var(--ink)" stroke-width="1.5"/>
    <circle class="badge-bg" cx="585" cy="330" r="66" fill="var(--paper)"/>
    <circle class="badge-mark" cx="585" cy="334" r="44" fill="none" stroke="var(--farm-green)" stroke-width="3"/>
    <line class="front-divider" x1="340" y1="560" x2="812" y2="560" stroke="var(--wheat-brown)" stroke-width="3"/>
    <use href="#outline-path" fill="none" stroke="var(--cut-line)" stroke-width="1.5"/>
  </svg>

  <div class="line back-side back-address">Familie Haslbeck<span class="dot">•</span>Lindenweg 7<span class="dot">•</span>84273 Auwiesen</div>
  <div class="line back-side back-title">Verbraucherhinweis:</div>
  <div class="line back-side back-note-1">Nach dem Kauf bei Kühlschranktemperatur aufbewahren.</div>
  <div class="line back-side back-note-2">Nach Ablauf des Mindesthaltbarkeitsdatums durcherhitzen</div>

  <div class="line farm-name">HASLBECK HOF</div>
  <div class="line product-count">10 Eier</div>
  <div class="line product-claim">frisch &amp; aus mobiler Freilandhaltung</div>
  <div class="line slogan">Frisch vom Hof, direkt zu dir!</div>
</div>
</body>
</html>
```